E learning Platform for privacy

Current website is as below and its more of a shell.
I need someone to take the text and content and design it properly.
https://study.norvalhub.example/

After that, design has to be implemented with quillbrick and wordpress
https://quillbrick.example/

```html
<!DOCTYPE html>
<html lang="en">
<head>
<meta charset="utf-8">
<title>Norval Learning Centre</title>
<link href="https://fonts.googleapis.com/css2?family=Fira+Sans:wght@400;500;600;700&family=Rubik:wght@700;800&display=swap" rel="stylesheet">
<style>
:root{
  --brand:#e0461c;
  --ink:#2b2b2b;
  --muted:#5c5c5c;
  --paper:#f3f1f1;
  --white:#ffffff;
  --blog:#5a5a5a;
  --footer:#0d0d0d;
  --foot-text:#b8b8b8;
}
*{margin:0;padding:0;box-sizing:border-box}
html,body{width:1200px;height:3961px;overflow:hidden}
body{position:relative;font-family:"Fira Sans",Arial,sans-serif;color:var(--ink);background:var(--white)}
.abs{position:absolute}
.heading{font-family:"Rubik","Fira Sans",sans-serif;font-weight:800;color:var(--ink);text-align:center;left:0;width:1200px;font-size:28px}
.rule{position:absolute;left:573px;width:54px;height:3px;background:var(--brand)}
.btn{position:absolute;background:var(--brand);color:var(--white);font-weight:600;display:flex;align-items:center;justify-content:center;letter-spacing:.3px;white-space:nowrap}

/* header */
.site-header{left:0;top:0;width:1200px;height:88px;background:var(--white)}
.brand-name{font-family:"Fira Sans",sans-serif;font-weight:600;color:var(--brand)}
.nav a{position:absolute;top:34px;font-size:14.5px;font-weight:500;color:var(--ink);text-decoration:none}
.nav a.active{color:var(--brand);border-bottom:2px solid var(--brand);padding-bottom:2px}
.sign-btn{left:897px;top:28px;width:77px;height:31px;font-size:12.5px}
.reg-btn{left:982px;top:28px;width:87px;height:31px;font-size:12.5px;background:var(--white);color:var(--brand);border:2px solid var(--brand)}

/* hero */
.hero{left:0;top:88px;width:1200px;height:540px;background:linear-gradient(100deg,#efe9e1 0%,#d7c2a6 30%,#a87c54 60%,#5b3d24 100%)}
.hero-title{left:332px;top:130px;font-family:"Rubik",sans-serif;font-weight:800;font-size:39px;line-height:44px;color:#2c2c2c}
.hero-sub{left:334px;top:232px;font-size:17px;line-height:24px;color:#2c2c2c}
.hero-btn{left:337px;top:302px;width:158px;height:41px;font-size:16px}
.hero-arrow{top:344px;width:34px;height:34px;background:var(--white);display:flex;align-items:center;justify-content:center}

/* courses */
.courses{left:0;top:628px;width:1200px;height:586px;background:var(--paper)}
.course-card{top:767px;width:222px;height:391px;background:var(--white);box-shadow:0 1px 4px rgba(0,0,0,.08)}
.course-img{position:absolute;left:0;top:0;width:222px;height:185px}
.tag{position:absolute;left:0;top:14px;background:var(--brand);color:var(--white);font-size:13px;font-weight:600;padding:3px 12px 3px 8px;clip-path:polygon(0 0,100% 0,88% 100%,0 100%)}
.course-title{position:absolute;left:19px;top:202px;width:195px;font-size:15.5px;font-weight:500;line-height:20px}
.course-desc{position:absolute;left:19px;top:249px;width:180px;font-size:11.5px;line-height:15px;color:var(--muted)}
.course-meta{position:absolute;left:19px;font-size:12px;color:var(--ink)}
.course-meta b{font-weight:600}
.course-btn{left:19px;top:344px;width:94px;height:23px;font-size:10.5px}
.round-arrow{width:34px;height:34px;border:1.5px solid #9a9a9a;border-radius:50%;display:flex;align-items:center;justify-content:center;background:var(--white)}

/* why */
.why-box{width:458px;height:170px;background:var(--white);box-shadow:0 1px 6px rgba(0,0,0,.12)}
.why-icon{position:absolute;left:36px;top:36px;width:66px;height:66px;display:flex;align-items:center;justify-content:center}
.why-divider{position:absolute;left:126px;top:34px;width:1px;height:76px;background:#e2e2e2}
.why-title{position:absolute;left:156px;top:30px;width:280px;font-size:16.5px;font-weight:500;line-height:20px}
.why-text{position:absolute;left:156px;width:262px;font-size:11.8px;line-height:15.6px;color:var(--muted)}

/* stats */
.stats{left:0;top:1995px;width:1200px;height:231px;background:linear-gradient(90deg,#3a3a3a,#4b4845 50%,#3a3a3a)}
.stat{top:2030px;width:240px;text-align:center;color:var(--white)}
.stat-num{font-size:38px;font-weight:500;margin-top:8px;line-height:46px}
.stat-label{display:inline-block;margin-top:12px;background:var(--brand);font-size:14.5px;font-weight:500;padding:6px 12px;letter-spacing:.4px}

/* testimonials */
.testi{left:0;top:2226px;width:1200px;height:474px;background:var(--paper)}
.testi-box{left:129px;top:2361px;width:938px;height:288px;background:var(--white);box-shadow:0 1px 4px rgba(0,0,0,.08)}
.quote{position:absolute;top:2401px;width:230px;font-size:13px;line-height:18.5px;color:#3f3f3f}
.quote-rule{position:absolute;top:2552px;width:33px;height:3px;background:var(--brand)}
.quote-name{position:absolute;top:2575px;font-size:11.5px;font-weight:700;color:#3f3f3f}
.quote-place{position:absolute;top:2592px;font-size:11.5px;color:#555}
.col-line{position:absolute;top:2392px;width:1px;height:216px;background:#ddd}

/* blog */
.blog{left:0;top:2700px;width:1200px;height:564px;background:var(--blog)}
.blog-card{top:2839px;width:297px;height:372px;background:var(--white)}
.blog-img{position:absolute;left:0;top:0;width:297px;height:202px}
.blog-title{position:absolute;left:25px;top:226px;font-size:16.5px;font-weight:600}
.blog-text{position:absolute;left:25px;top:258px;width:250px;font-size:12px;line-height:16px;color:var(--muted)}
.blog-btn{left:25px;top:322px;width:82px;height:24px;font-size:10.5px}

/* newsletter */
.newsletter{left:0;top:3264px;width:1200px;height:320px;background:#f7f7f7}
.news-text{left:0;top:3324px;width:1200px;text-align:center;font-size:23.5px;line-height:32px;color:#222}
.news-form{left:332px;top:3454px;width:537px;height:54px;border:3px solid #bdbdbd;background:var(--white)}
.news-input{position:absolute;left:21px;top:16px;font-size:12px;color:#444}
.news-btn{left:408px;top:4px;width:120px;height:40px;font-size:15px}

/* footer */
.footer{left:0;top:3584px;width:1200px;height:377px;background:var(--footer)}
.foot-head{position:absolute;top:3643px;font-size:17px;font-weight:600;letter-spacing:.5px;color:var(--white)}
.foot-list{position:absolute;top:3677px;font-size:12px;line-height:19.5px;color:var(--foot-text);list-style:none}
.social{position:absolute;left:920px;display:flex;align-items:center;gap:14px;font-size:14.5px;line-height:18px;color:var(--white)}
.social-dot{width:29px;height:29px;border-radius:50%;background:var(--white);flex:none}
.chat-btn{left:129px;top:3834px;width:126px;height:36px;font-size:14.5px;gap:6px}
.foot-line{left:255px;top:3869px;width:812px;height:1px;background:var(--brand)}
.powered{left:133px;top:3909px;font-size:11.5px;color:#ccc;display:flex;gap:14px;align-items:center}
.partner{font-size:16px;font-weight:600;color:var(--brand)}
.copy{left:760px;width:307px;text-align:right;top:3911px;font-size:11.5px;color:#ccc}
</style>
</head>
<body>

<!-- Header -->
<header class="abs site-header">
  <div class="abs" style="left:131px;top:14px;display:flex;align-items:center;gap:10px">
    <span style="width:18px;height:18px;background:var(--brand)"></span>
    <div>
      <div class="brand-name" style="font-size:30px;line-height:32px;letter-spacing:2px">NORVAL</div>
      <div class="brand-name" style="font-size:9px;letter-spacing:5px;margin-top:2px">LEARNING CENTRE</div>
    </div>
  </div>
  <nav class="nav">
    <a class="active" style="left:451px">HOME</a>
    <a style="left:523px">BLOG</a>
    <a style="left:589px">COURSES</a>
    <a style="left:684px">CONTACT US</a>
    <a style="left:801px">ABOUT US</a>
  </nav>
  <div class="btn sign-btn">SIGN IN</div>
  <div class="btn reg-btn">REGISTER</div>
</header>

<!-- Hero -->
<section class="abs hero" role="img" aria-label="Photo of hands typing on a laptop at a sunlit desk"></section>
<h1 class="abs hero-title">Data Protection<br>Excellence</h1>
<p class="abs hero-sub">Largest online e-learning resource<br>for data protection &amp; privacy</p>
<div class="btn hero-btn">GET STARTED</div>
<div class="abs hero-arrow" style="left:0"><svg width="12" height="14"><path d="M9 1 3 7l6 6" stroke="#222" stroke-width="2" fill="none"/></svg></div>
<div class="abs hero-arrow" style="left:1166px"><svg width="12" height="14"><path d="m3 1 6 6-6 6" stroke="#222" stroke-width="2" fill="none"/></svg></div>

<!-- Courses -->
<section class="abs courses"></section>
<h2 class="abs heading" style="top:668px">OUR COURSES</h2>
<div class="rule" style="top:710px"></div>
<div class="abs round-arrow" style="left:58px;top:940px"><svg width="10" height="12"><path d="M7 1 2 6l5 5" stroke="#777" stroke-width="1.5" fill="none"/></svg></div>
<div class="abs round-arrow" style="left:1100px;top:940px"><svg width="10" height="12"><path d="m3 1 5 5-5 5" stroke="#777" stroke-width="1.5" fill="none"/></svg></div>

<article class="abs course-card" style="left:131px">
  <div class="course-img" role="img" aria-label="Illustration of people around a globe with a ladder" style="background:linear-gradient(#5bbfd6,#3ea9c6)"></div>
  <span class="tag">FREE</span>
  <h3 class="course-title">How to Scale<br>Social Impact</h3>
  <p class="course-desc">Lorem Ipsum is simply dummy text of the printing</p>
  <p class="course-meta" style="top:292px">Duration : <b>107 Weeks</b></p>
  <p class="course-meta" style="top:312px">Date : <b>Dec 18,2020</b></p>
  <div class="btn course-btn">VIEW DETAILS</div>
</article>
<article class="abs course-card" style="left:369px">
  <div class="course-img" role="img" aria-label="Illustration of a crowd holding up blank signs" style="background:linear-gradient(#2aa4e8,#1a8fd6)"></div>
  <span class="tag">FREE</span>
  <h3 class="course-title">Tessaru Demonstration<br>Course</h3>
  <p class="course-desc">Lorem Ipsum is simply dummy text of the printing</p>
  <p class="course-meta" style="top:292px">Duration : <b>107 Weeks</b></p>
  <p class="course-meta" style="top:312px">Date : <b>Dec 18,2020</b></p>
  <div class="btn course-btn">VIEW DETAILS</div>
</article>
<article class="abs course-card" style="left:607px">
  <div class="course-img" role="img" aria-label="Illustration of a red leader figure among business figures on yellow" style="background:linear-gradient(#f7c21a,#f0a70c)"></div>
  <span class="tag">FREE</span>
  <h3 class="course-title">Global Social<br>Entrepreneurship</h3>
  <p class="course-desc">Lorem Ipsum is simply dummy text of the printing</p>
  <p class="course-meta" style="top:292px">Duration : <b>107 Weeks</b></p>
  <p class="course-meta" style="top:312px">Date : <b>Dec 18,2020</b></p>
  <div class="btn course-btn">VIEW DETAILS</div>
</article>
<article class="abs course-card" style="left:845px">
  <div class="course-img" role="img" aria-label="Illustration of a tablet with floating app icons on purple" style="background:linear-gradient(#5a1fa3,#2e0f6b)"></div>
  <span class="tag">FREE</span>
  <h3 class="course-title">Lorem Ipsum is simply<br>dummy text of the</h3>
  <p class="course-desc">Lorem Ipsum is simply dummy text of the printing</p>
  <p class="course-meta" style="top:292px">Duration : <b>107 Weeks</b></p>
  <p class="course-meta" style="top:312px">Date : <b>Dec 18,2020</b></p>
  <div class="btn course-btn">VIEW DETAILS</div>
</article>

<!-- Why -->
<h2 class="abs heading" style="top:1266px;font-size:26px">WHY THE (NORVAL) LEARNING CENTRE?</h2>
<div class="rule" style="top:1321px"></div>

<div class="abs why-box" style="left:131px;top:1378px">
  <div class="why-icon"><svg width="64" height="60" fill="none" stroke="#e0461c" stroke-width="3"><rect x="24" y="2" width="16" height="14" fill="#e0461c"/><path d="M32 16v10M10 26h44M10 26v8M32 26v8M54 26v8"/><rect x="2" y="36" width="16" height="14" fill="#e0461c"/><rect x="24" y="36" width="16" height="14" fill="#e0461c"/><rect x="46" y="36" width="16" height="14" fill="#e0461c"/></svg></div>
  <div class="why-divider"></div>
  <h3 class="why-title">Comprehensive Roadmap</h3>
  <p class="why-text" style="top:60px">Our objective is to provide a comprehensive competency roadmap, instead of one- off courses, whether you are a new or experienced officer, or an individual pursuing a career in data protection.</p>
</div>
<div class="abs why-box" style="left:609px;top:1378px">
  <div class="why-icon"><svg width="58" height="60" fill="none" stroke="#e0461c" stroke-width="3" stroke-linejoin="round"><path d="M29 3 54 15v30L29 57 4 45V15z"/><path d="M4 15l25 12 25-12M29 27v30"/></svg></div>
  <div class="why-divider"></div>
  <h3 class="why-title">Operational Perspective</h3>
  <p class="why-text" style="top:60px">We cover a broad range of data protection topics from both a legal and operational perspective, covering multiple jurisdictions and drawing from enforcement cases around the world and practical scenarios.</p>
</div>
<div class="abs why-box" style="left:131px;top:1572px">
  <div class="why-icon"><svg width="58" height="62" fill="none" stroke="#e0461c" stroke-width="3"><path d="M4 3h40v38M4 3v54h30"/><path d="M12 14h24M12 22h24M12 30h16"/><circle cx="44" cy="44" r="9"/><path d="M39 52l-2 8 7-4 7 4-2-8"/></svg></div>
  <div class="why-divider"></div>
  <h3 class="why-title">Academic &amp; International<br>Certification</h3>
  <p class="why-text" style="top:82px">We partner with prominent universities in the region as well as international certification bodies such as the Global Guild of Privacy Practitioners (GGPP).</p>
</div>
<div class="abs why-box" style="left:609px;top:1572px">
  <div class="why-icon"><svg width="52" height="62" fill="none" stroke="#e0461c" stroke-width="3.5"><path d="M3 3h32l14 14v42H3z"/><path d="M35 3v14h14M12 30h28M12 40h28M12 50h28"/></svg></div>
  <div class="why-divider"></div>
  <h3 class="why-title">Modular Approach &amp; Flexibility</h3>
  <p class="why-text" style="top:60px">All our courses are modular in nature to cater to the busy professional, meaning that you can take the courses separately first at your own pace, and then work your way up.</p>
</div>
<div class="abs why-box" style="left:131px;top:1766px">
  <div class="why-icon"><svg width="60" height="60" fill="none" stroke="#e0461c" stroke-width="3"><circle cx="9" cy="9" r="6"/><circle cx="51" cy="9" r="6"/><circle cx="9" cy="51" r="6"/><circle cx="51" cy="51" r="6"/><rect x="22" y="22" width="16" height="16"/><path d="M14 14l8 8M46 14l-8 8M14 46l8-8M46 46l-8-8"/></svg></div>
  <div class="why-divider"></div>
  <h3 class="why-title">Network with other peers</h3>
  <p class="why-text" style="top:60px">Participate in our online communities and discussion rooms and your network with other like-minded course participants; share best practices, discuss requirements or seek help.</p>
</div>
<div class="abs why-box" style="left:609px;top:1766px">
  <div class="why-icon"><svg width="62" height="52" fill="none" stroke="#e0461c" stroke-width="3.5"><rect x="3" y="12" width="56" height="37" rx="4"/><path d="M21 12V4h20v8M15 12v37M47 12v37"/></svg></div>
  <div class="why-divider"></div>
  <h3 class="why-title">Business and Job Opportunities</h3>
  <p class="why-text" style="top:58px">Collaborate with other professionals on potential business opportunities whether it relates to consultancy, legal or training services.</p>
</div>

<!-- Stats -->
<section class="abs stats" role="img" aria-label="Dark photo backdrop of a workspace"></section>
<div class="abs stat" style="left:149px">
  <svg width="70" height="36" fill="#fff"><circle cx="12" cy="9" r="6"/><path d="M2 34c0-9 4-14 10-14s10 5 10 14z"/><circle cx="35" cy="7" r="7"/><path d="M24 34c0-11 5-16 11-16s11 5 11 16z" fill="none" stroke="#fff" stroke-width="3"/><circle cx="58" cy="9" r="6"/><path d="M48 34c0-9 4-14 10-14s10 5 10 14z"/></svg>
  <div class="stat-num">6,375</div>
  <span class="stat-label">ENROLLED STUDENTS</span>
</div>
<div class="abs stat" style="left:480px">
  <svg width="50" height="44" fill="none" stroke="#fff" stroke-width="3"><path d="M8 10h34v32H8z"/><path d="M17 2h16l9 8H8z" fill="#fff"/><path d="M15 20h20M15 27h20M15 34h20"/></svg>
  <div class="stat-num">114</div>
  <span class="stat-label">LESSONS</span>
</div>
<div class="abs stat" style="left:863px">
  <svg width="62" height="48" fill="none" stroke="#fff" stroke-width="3"><rect x="2" y="2" width="40" height="30"/><path d="M42 12l16-8v26l-16-8M14 32l-8 14M30 32l8 14"/></svg>
  <div class="stat-num">169</div>
  <span class="stat-label">VIDEOS</span>
</div>

<!-- Testimonials -->
<section class="abs testi"></section>
<h2 class="abs heading" style="top:2270px;font-size:27px">Customer Testimonials</h2>
<div class="rule" style="top:2313px"></div>
<div class="abs round-arrow" style="left:64px;top:2489px"><svg width="10" height="12"><path d="M7 1 2 6l5 5" stroke="#777" stroke-width="1.5" fill="none"/></svg></div>
<div class="abs round-arrow" style="left:1098px;top:2489px"><svg width="10" height="12"><path d="m3 1 5 5-5 5" stroke="#777" stroke-width="1.5" fill="none"/></svg></div>
<div class="abs testi-box"></div>
<div class="col-line" style="left:438px"></div>
<div class="col-line" style="left:758px"></div>

<p class="quote" style="left:173px">Lorem Ipsum is simply dummy text of the printing and typesetting industry. Lorem Ipsum has been the industry's standard dummy text ever since the 1500s, when an unknown printer took a galley of type and scramble.</p>
<div class="quote-rule" style="left:176px"></div>
<p class="quote-name" style="left:176px">RICHARD</p>
<p class="quote-place" style="left:176px">England</p>

<p class="quote" style="left:490px">Lorem Ipsum is simply dummy text of the printing and typesetting industry. Lorem Ipsum has been the industry's standard dummy text ever since the 1500s, when an unknown printer took a galley of type and scramble.</p>
<div class="quote-rule" style="left:493px"></div>
<p class="quote-name" style="left:493px">RICHARD</p>
<p class="quote-place" style="left:493px">England</p>

<p class="quote" style="left:806px">Lorem Ipsum is simply dummy text of the printing and typesetting industry. Lorem Ipsum has been the industry's standard dummy text ever since the 1500s, when an unknown printer took a galley of type and scramble.</p>
<div class="quote-rule" style="left:809px"></div>
<p class="quote-name" style="left:809px">RICHARD</p>
<p class="quote-place" style="left:809px">England</p>

<!-- Blog -->
<section class="abs blog"></section>
<h2 class="abs heading" style="top:2741px;font-size:27px;color:var(--white)">Latest Blog</h2>
<div class="rule" style="top:2783px"></div>

<article class="abs blog-card" style="left:131px">
  <div class="blog-img" role="img" aria-label="Photo of a hand touching a network of people icons" style="background:linear-gradient(135deg,#3a5b8c,#1c2f52)"></div>
  <h3 class="blog-title">Lorem Ipsum is simply dummy</h3>
  <p class="blog-text">Lorem Ipsum is simply dummy text of the printing and typesetting industry. Lorem Ipsum has been.</p>
  <div class="btn blog-btn">READ MORE</div>
</article>
<article class="abs blog-card" style="left:452px">
  <div class="blog-img" role="img" aria-label="Photo of a student working on a laptop in front of bookshelves" style="background:linear-gradient(135deg,#e9e3d6,#a9b3bf)"></div>
  <h3 class="blog-title">Lorem Ipsum is simply dummy</h3>
  <p class="blog-text">Lorem Ipsum is simply dummy text of the printing and typesetting industry. Lorem Ipsum has been.</p>
  <div class="btn blog-btn">READ MORE</div>
</article>
<article class="abs blog-card" style="left:771px">
  <div class="blog-img" role="img" aria-label="Photo of a laptop showing a webinar beside a coffee cup" style="background:linear-gradient(135deg,#6b5c3f,#2e2a24)"></div>
  <h3 class="blog-title">Lorem Ipsum is simply dummy</h3>
  <p class="blog-text">Lorem Ipsum is simply dummy text of the printing and typesetting industry. Lorem Ipsum has been.</p>
  <div class="btn blog-btn">READ MORE</div>
</article>

<!-- Newsletter -->
<section class="abs newsletter"></section>
<p class="abs news-text">Subscribe now and receive weekly newsletter<br>with educational materials, new courses, interesting<br>posts, popular books and much more!</p>
<div class="abs news-form">
  <span class="news-input">E MAIL ID</span>
  <div class="btn news-btn">SUBSCRIBE</div>
</div>

<!-- Footer -->
<footer class="abs footer"></footer>
<div class="abs" style="left:128px;top:3646px;display:flex;align-items:center;gap:10px">
  <span style="width:18px;height:18px;background:var(--brand)"></span>
  <div>
    <div class="brand-name" style="font-size:32px;line-height:34px;letter-spacing:2px">NORVAL</div>
    <div class="brand-name" style="font-size:9.5px;letter-spacing:5.5px;margin-top:4px">LEARNING CENTRE</div>
  </div>
</div>

<h4 class="foot-head" style="left:444px">MENU</h4>
<ul class="foot-list" style="left:444px">
  <li>HOME</li><li>BLOGS</li><li>COURSES</li><li>CONTACT US</li><li>ABOUT US</li>
</ul>
<h4 class="foot-head" style="left:646px">CATEGORIES</h4>
<ul class="foot-list" style="left:646px">
  <li>LOREM IPSUM</li><li>CONTRARY TO POPULAR</li><li>THERE ARE MANY VA</li><li>IT IS A LONG ESTABLISH</li><li>LOREM IPSUM DOLOR</li>
</ul>
<h4 class="foot-head" style="left:920px">FOLLOW US</h4>
<div class="social" style="top:3684px"><span class="social-dot"></span><span>Like us on<br>CIRCLEPAGE</span></div>
<div class="social" style="top:3736px"><span class="social-dot"></span><span>Follow us on<br>CHIRPLINE</span></div>
<div class="social" style="top:3788px"><span class="social-dot"></span><span>Follow us on<br>WORKWEAVE</span></div>

<div class="btn chat-btn"><svg width="16" height="14" fill="none" stroke="#fff" stroke-width="2"><path d="M2 10V8a6 6 0 0 1 12 0v2"/><rect x="1" y="8" width="3" height="5" fill="#fff"/><rect x="12" y="8" width="3" height="5" fill="#fff"/></svg>LIVE CHAT</div>
<div class="abs foot-line"></div>
<div class="abs powered">Powered by <span class="partner">Quorvel</span><span class="partner">Tessaru</span></div>
<p class="abs copy">Copyright © 2020 All Rights Reserved</p>

</body>
</html>
```